Small but growing painting company. Have built up a steady client base. Want to start having a more professional look. Want to start with changing my business cards, and also getting new logo and tee shirts.

Target Market(s)

Home owners, property management companies, all ages 30-70

Industry/Entity Type

Painting And Decorating

Contact Information for Business Card

Bright Ridge Painting LLC Mark Delvecchi 630-584-3907 interior, exterior, vaulted ceiling, drywall repair, pressure washing, kitchen cabinets, epoxy, garage floors,

Font styles to use
Sans Serif
Other font styles liked:
• Harrington

Colors
0355a3
ffffff
ec1f27
000000
3176b5
0493ce
474747
b7b7b7

Requirements
Must have
• Creative, something that doesn’t look like every other painting card.
Nice to have
• I would like something with an arrow or something going to a point

```html
<!DOCTYPE html>
<html lang="en">
<head>
<meta charset="utf-8">
<title>Bright Ridge Painting LLC – Business Card</title>
<link rel="stylesheet" href="https://fonts.googleapis.com/css2?family=Work+Sans:wght@400;500;600&display=swap">
<style>
  :root {
    --page-bg: #e4e7eb;
    --card-bg: #f7f8f9;
    --brand-blue: #0355a3;
    --name-blue: #1b3f7e;
    --line-blue: #3a5b93;
    --band-black: #111111;
    --text-dark: #2a2a2a;
    --icon-grey: #474747;
  }
  * { box-sizing: border-box; margin: 0; padding: 0; }
  html, body {
    width: 1200px; height: 900px; overflow: hidden;
    background: var(--page-bg);
    font-family: "Work Sans", Arial, sans-serif;
  }
  .card {
    position: absolute; left: 180px; top: 210px;
    width: 840px; height: 480px;
    background: var(--card-bg);
    box-shadow: 0 10px 30px rgba(0,0,0,0.12);
    overflow: hidden;
  }
  .brand {
    position: absolute; left: 40px; top: 60px;
    display: flex; align-items: center; gap: 14px;
  }
  .brand-mark {
    width: 54px; height: 54px; background: var(--brand-blue);
  }
  .brand-name {
    font-size: 30px; font-weight: 600; line-height: 1.1;
    color: var(--brand-blue); width: 260px;
  }
  .person {
    position: absolute; right: 40px; top: 225px; text-align: right;
  }
  .person-name {
    font-size: 33px; font-weight: 500; color: var(--name-blue);
    letter-spacing: 0.5px; text-transform: uppercase;
  }
  .person-title {
    font-size: 18px; color: var(--text-dark); margin-top: 2px;
  }
  .divider {
    position: absolute; left: 40px; right: 40px; top: 310px;
    height: 1.5px; background: var(--line-blue);
  }
  .contacts {
    position: absolute; left: 40px; top: 344px;
    list-style: none; font-size: 19px; color: var(--text-dark);
  }
  .contacts li { display: flex; align-items: center; gap: 10px; height: 27px; }
  .contacts svg { width: 12px; height: 12px; fill: none; stroke: var(--icon-grey); stroke-width: 1.6; }
  .address {
    position: absolute; right: 40px; top: 371px;
    font-style: normal; text-align: right;
    font-size: 19px; line-height: 27px; color: var(--text-dark);
  }
  .footer-band { position: absolute; left: 0; bottom: 0; width: 840px; height: 60px; }
</style>
</head>
<body>
  <div class="card">
    <div class="brand">
      <span class="brand-mark"></span>
      <span class="brand-name">Bright Ridge Painting LLC</span>
    </div>

    <div class="person">
      <p class="person-name">Mark Delvecchi</p>
      <p class="person-title">Director</p>
    </div>

    <div class="divider"></div>

    <ul class="contacts">
      <li>
        <svg viewBox="0 0 12 12"><path d="M3 1 L5 3.5 L3.8 5 Q5 7.5 7 8.2 L8.5 7 L11 9 L9.5 11 Q3 10 1 2.5 Z"/></svg>
        630-584-3907
      </li>
      <li>
        <svg viewBox="0 0 12 12"><rect x="1" y="2.5" width="10" height="7"/><path d="M1 2.5 L6 6.5 L11 2.5"/></svg>
        hello@brightridgepainting.com
      </li>
      <li>
        <svg viewBox="0 0 12 12"><circle cx="6" cy="6" r="5"/><path d="M1 6 H11 M6 1 Q3 6 6 11 M6 1 Q9 6 6 11"/></svg>
        www.brightridgepainting.com
      </li>
    </ul>

    <address class="address">
      412 Alder Lane<br>
      Naperville, IL 60540
    </address>

    <svg class="footer-band" viewBox="0 0 840 60" aria-hidden="true">
      <path d="M150 24 H425 Q450 24 470 14 Q485 7 505 7 H840" fill="none" stroke="var(--line-blue)" stroke-width="4"/>
      <path d="M430 60 Q470 60 490 38 Q505 22 530 22 H840 V60 Z" fill="var(--band-black)"/>
    </svg>
  </div>
</body>
</html>
```